Coffee label for coffee brand - Kiln Lantern coffee

We want someone to design a label for packaging of a coffee line. The design will then be printed on stickers.

It is called Kiln Lantern Coffee (logo enclosed) I want to incorporate a streetscape and the idea is that with every different coffee it will be a different colour (we have 6 varieties at the moment) with a black background. It needs to have a modern feel.

It needs to have a blank area towards the bottom for the type of coffee which we will print later on)

text to include

'Roasting exceptional coffee'

Target Market(s)

Coffee drinkers - modern feel

Font styles to use
Sans Serif

Colors
f78f20
9bcb3b
33a6d7
b768aa

Requirements
Must have
• the logo incorporated
• Space for coffee variety
• Quote' Roasting exceptional coffee'
Nice to have
• Streetscape theme incorporated - bright colour varieties (would love metallic) (on black background)

```html
<!DOCTYPE html>
<html lang="en">
<head>
<meta charset="utf-8">
<title>Kiln Lantern Coffee – Pouch Labels</title>
<link rel="stylesheet" href="https://fonts.googleapis.com/css2?family=Montserrat:wght@500;600&family=Oswald:wght@500;600&display=swap">
<style>
  :root {
    --page: #ffffff;
    --label-black: #0b0b0b;
    --ink: #111111;
    --paper-light: #ffffff;
    --silver: #e4e4e4;
    --silver-deep: #cfcfcf;
    --orchid: #d672d6;
    --orchid-deep: #b44fb8;
    --badge-orchid: #a855a8;
    --bean-dark: #3b2014;
    --bean-mid: #7a4428;
    --bean-light: #b0714a;
  }
  * { box-sizing: border-box; margin: 0; padding: 0; }
  html, body {
    width: 1200px; height: 1200px; overflow: hidden;
    background: var(--page);
  }
  .canvas { position: relative; width: 1200px; height: 1200px; }

  .label {
    position: absolute;
    width: 460px; height: 690px;
    overflow: hidden;
    background: var(--label-black);
    border-radius: 4px 4px 18px 18px;
  }
  .label--silver { left: 115px; top: 275px; }
  .label--orchid { left: 660px; top: 372px; }

  .label__top {
    position: absolute; left: 0; top: 0; width: 100%; height: 340px;
    background: linear-gradient(135deg, #000 0%, #161616 60%, #050505 100%);
  }
  .label__bottom {
    position: absolute; left: 0; top: 340px; width: 100%; height: 350px;
  }
  .label--silver .label__bottom { background: linear-gradient(180deg, var(--silver) 0%, #f2f2f2 60%, var(--silver-deep) 100%); }
  .label--orchid .label__bottom { background: linear-gradient(180deg, var(--orchid-deep) 0%, var(--orchid) 45%, var(--orchid-deep) 100%); }

  .brand {
    position: absolute; left: 0; top: 150px; width: 100%;
    display: flex; align-items: center; justify-content: center; gap: 12px;
    font-family: "Oswald", sans-serif; font-weight: 600;
    font-size: 40px; letter-spacing: 1px; text-transform: uppercase;
    color: var(--paper-light);
  }
  .brand__dot {
    width: 14px; height: 14px; border-radius: 50%;
    background: var(--paper-light);
  }

  .weight {
    position: absolute; top: 388px;
    font-family: "Montserrat", sans-serif; font-weight: 600; font-size: 17px;
    color: var(--ink);
  }
  .weight--oz { left: 52px; }
  .weight--grams { right: 48px; }

  .beans {
    position: absolute; left: 0; top: 450px; width: 100%; height: 150px;
    background: linear-gradient(90deg, var(--bean-dark), var(--bean-light) 20%, var(--bean-mid) 40%, var(--bean-light) 55%, var(--bean-dark) 70%, var(--bean-light) 85%, var(--bean-mid));
  }

  .badge {
    position: absolute; left: 140px; top: 312px;
    width: 180px; height: 180px; border-radius: 50%;
    display: flex; align-items: center; justify-content: center;
    text-align: center;
  }
  .label--silver .badge { background: var(--silver); }
  .label--orchid .badge { background: var(--badge-orchid); }
  .badge__rings { position: absolute; inset: 0; }
  .badge__quote {
    position: relative;
    font-family: "Montserrat", sans-serif; font-weight: 600;
    font-size: 17px; line-height: 1.4; text-transform: uppercase;
    color: var(--ink);
  }

  .info {
    position: absolute; left: 0; top: 618px; width: 100%; text-align: center;
    font-family: "Oswald", sans-serif; font-weight: 500;
    font-size: 28px; text-transform: uppercase; color: var(--ink);
  }
</style>
</head>
<body>
<main class="canvas">

  <section class="label label--silver">
    <div class="label__top"></div>
    <div class="label__bottom"></div>
    <div class="brand"><span class="brand__dot"></span>Kiln Lantern Coffee</div>
    <span class="weight weight--oz">12.OZ</span>
    <span class="weight weight--grams">340 G</span>
    <div class="beans" role="img" aria-label="Row of roasted coffee beans"></div>
    <div class="badge">
      <svg class="badge__rings" viewBox="0 0 180 180" aria-hidden="true">
        <path d="M30 62 A68 68 0 0 1 148 58" fill="none" stroke="#111" stroke-width="2.5" stroke-linecap="round"/>
        <path d="M158 82 A68 68 0 0 1 146 128" fill="none" stroke="#111" stroke-width="2" stroke-linecap="round"/>
        <path d="M26 110 A68 68 0 0 0 120 152" fill="none" stroke="#111" stroke-width="2.5" stroke-linecap="round"/>
      </svg>
      <p class="badge__quote">Roasting<br>Exceptional<br>Cofee</p>
    </div>
    <p class="info">Products Info</p>
  </section>

  <section class="label label--orchid">
    <div class="label__top"></div>
    <div class="label__bottom"></div>
    <div class="brand"><span class="brand__dot"></span>Kiln Lantern Coffee</div>
    <span class="weight weight--oz">12.OZ</span>
    <span class="weight weight--grams">340 G</span>
    <div class="beans" role="img" aria-label="Row of roasted coffee beans"></div>
    <div class="badge">
      <svg class="badge__rings" viewBox="0 0 180 180" aria-hidden="true">
        <path d="M30 62 A68 68 0 0 1 148 58" fill="none" stroke="#111" stroke-width="2.5" stroke-linecap="round"/>
        <path d="M158 82 A68 68 0 0 1 146 128" fill="none" stroke="#111" stroke-width="2" stroke-linecap="round"/>
        <path d="M26 110 A68 68 0 0 0 120 152" fill="none" stroke="#111" stroke-width="2.5" stroke-linecap="round"/>
      </svg>
      <p class="badge__quote">Roasting<br>Exceptional<br>Cofee</p>
    </div>
    <p class="info">Products Info</p>
  </section>

</main>
</body>
</html>
```